Jobinserat Vorlage medizinischer Bereich
Sehr gute Kommunikation auch mit Rückfragen damit das Projekt komplett verstanden wurde. Schnelle Umsetzung mit tollen Vorschlägen. Nur zu empfehlen!
Zielgruppe
Personalagentur im medizinischen Bereich (Krankenpfleger/Fachärzte)
Zielgruppe: Jobsuchende Krankenpflege Fachleute in Deutschland für die Schweiz!
Aufgabenstellung
jung, frisch, emotionell, verlockend
Bitte Text beachten: klinikpflegeleiterin
Wir benötigen ein Layout für ein Stelleninserat welches wir auf bei www.pflegestellenboerse.de platzieren möchten sowie auf www.medizinerkarriere.de / Das Format wird A4 sein, entweder eine oder zwei Seiten, je nachdem was für eine Stelle wir ausschreiben. Wichtig ist das Logo und der Text (siehe Projektanlage). Als Anhaltspunkt geht das Inserat (http://www.pflegestellenboerse.de/job/dipl-pflegefachfraudipl-pflegefachmann-hffh-oder-fage-fur-kurzeinsatze-10-20) in die Richtige Richtung, einfach mit unserer Farbe vom Logo oder der Academy http://www.valorintgruppe.com/academy/

```html
<!DOCTYPE html>
<html lang="de">
<head>
<meta charset="utf-8">
<title>Stelleninserat Klinikpflegeleitung</title>
<link href="https://fonts.googleapis.com/css2?family=Source+Sans+3:wght@400;600;700&display=swap" rel="stylesheet">
<style>
  :root {
    --accent: #e9a41a;
    --dark: #454545;
    --text: #2f2f2f;
    --paper: #ffffff;
    --backdrop: #ffffff;
    --edge: #d8d8d8;
  }
  * { box-sizing: border-box; margin: 0; padding: 0; }
  html, body { width: 1200px; height: 1200px; overflow: hidden; background: var(--backdrop); }
  body { font-family: "Source Sans 3", Arial, sans-serif; color: var(--text); }

  .ad-page {
    position: absolute; left: 242px; top: 95px;
    width: 716px; height: 1010px;
    background: var(--paper);
    border: 1px solid var(--edge);
    overflow: hidden;
  }
  .top-rule { position: absolute; left: 0; top: 0; width: 100%; height: 6px; background: var(--accent); }
  .hero-photo {
    position: absolute; left: 0; top: 6px; width: 100%; height: 286px;
    background: linear-gradient(180deg, #e6ecf1 0%, #cbd8e3 45%, #a3bad1 78%, #f4f6f8 100%);
  }
  .kicker {
    position: absolute; left: 0; top: 263px; width: 247px; height: 50px;
    background: var(--accent); color: var(--dark);
    font-size: 37px; font-weight: 600; line-height: 50px; padding-left: 28px;
  }
  .title-bar {
    position: absolute; left: 0; top: 319px; width: 100%; height: 49px;
    background: var(--dark); color: #fff;
    font-size: 29px; font-weight: 600; line-height: 49px; padding-left: 95px;
  }
  .content {
    position: absolute; left: 95px; top: 394px; width: 532px;
    font-size: 12.6px; line-height: 15px;
  }
  .section-head { font-weight: 700; font-size: 14px; line-height: 18px; margin-bottom: 7px; }
  .list { list-style: none; margin-bottom: 14px; }
  .list li { position: relative; padding-left: 15px; margin-bottom: 3px; }
  .list li::before {
    content: ""; position: absolute; left: 0; top: 4px;
    width: 6px; height: 6px; background: var(--accent);
  }
  .para { margin-top: 14px; }
  .para:first-of-type { margin-top: 22px; }
  .para strong { font-weight: 700; }

  .advisor {
    position: absolute; left: 95px; top: 878px;
    font-size: 12.6px; line-height: 15px;
  }
  .advisor .label { font-weight: 700; margin-bottom: 6px; }
  .social { margin-top: 12px; display: flex; align-items: center; gap: 6px; }
  .social .mark { width: 12px; height: 12px; background: var(--dark); display: inline-block; }

  .brand { position: absolute; left: 414px; top: 908px; width: 280px; }
  .brand-name {
    font-size: 34px; font-weight: 600; color: var(--accent); line-height: 40px;
  }
  .brand-address { margin-top: 12px; font-size: 9px; line-height: 11px; font-weight: 600; color: var(--text); }

  .bottom-rule { position: absolute; left: 0; bottom: 0; width: 100%; height: 7px; background: var(--dark); }
</style>
</head>
<body>
  <main class="ad-page">
    <div class="top-rule"></div>
    <div class="hero-photo" role="img" aria-label="Foto eines lächelnden Ärzte- und Pflegeteams in weissen Kitteln und blauer Kleidung vor einem hellen Klinikgebäude"></div>
    <div class="kicker">Wir suchen</div>
    <h1 class="title-bar">Klinikpflegeleiterin / Klinikpflegeleiter</h1>

    <section class="content">
      <h2 class="section-head">Ihre Aufgaben:</h2>
      <ul class="list">
        <li>Sicherstellung einer wirksamen, wirtschaftlichen und zweckmässigen Pflege und Betreuung</li>
        <li>Führung und Förderung der unterstellten Mitarbeitenden inklusive Stellenplanbewirtschaftung</li>
        <li>Mitwirkung bei der strategischen Weiterentwicklung von unternehmensweiten Projekten<br>und Kliniken</li>
        <li>Gewährleistung des Ausbildungsauftrages auf der Grund- und Tertiärstufe</li>
        <li>Qualitätssicherung und Prozessoptimierung gemäss der Unternehmensstrategie</li>
      </ul>

      <h2 class="section-head">Anfoderungen:</h2>
      <ul class="list">
        <li>Dipl. Pflegefachfrau/-mann HF, DN II, AKP, FH, DGKS</li>
        <li>Fundierte Führungserfahrung mit einer ausgewiesenen Managementweiterbildung auf<br>Fachhochschulniveau oder einer vergleichbaren Weiterbildung</li>
        <li>Hohe Patientenorientierung</li>
        <li>Konzeptionelle Fähigkeiten verbunden mit Innovationskraft und unternehmerischen Denken<br>und Handeln</li>
        <li>Kommunikative und teamorientierte Persönlichkeit mit betriebswirtschaftlichen und<br>organisatorischen Fähigkeiten</li>
        <li>Engagement für eine interdisziplinäre und interprofessionelle Zusammenarbeit mit einem<br>hohen Mass an Verantwortungsbereitschaft</li>
      </ul>

      <p class="para">Suchen Sie eine verantwortungsvolle Herausforderung in einem familiären, dynamischen Umfeld<br>mit attraktiven Entwicklungsmöglichkeiten?</p>
      <p class="para"><strong>Wir garantieren Ihnen absolute Diskretion.</strong></p>
      <p class="para">Für einen ersten vertraulichen Kontakt steht Ihnen Herr <strong>Lukas Brenner</strong> gerne zur Verfügung.<br>
        Zögern Sie nicht, wir freuen uns auf Ihre komplette online Bewerbung mit Foto per E-Mail an:<br>
        <strong>lukas.brenner@valorintgruppe.com</strong></p>
    </section>

    <section class="advisor">
      <p class="label">Ihr Berater:</p>
      <p>Lukas Brenner</p>
      <p>Tel. +41 44 555 01 23</p>
      <p>Mail: lukas.brenner@valorintgruppe.com</p>
      <p>Web: valorintgruppe.com</p>
      <p class="social">Finde uns auf <span class="mark"></span></p>
    </section>

    <section class="brand">
      <p class="brand-name">Valorint</p>
      <p class="brand-address">Valorint – Recruitment Group Ltd.<br>Lindenweg 4 | CH-6000 Musterdorf</p>
    </section>

    <div class="bottom-rule"></div>
  </main>
</body>
</html>
```